TIVARELCAP web-presence redisign

We would like to have our existing web-presence redesigned. Have a look at www.tivarel.ch (please use explorer). To the existing 11 pages we would add one more.

```html
<!DOCTYPE html>
<html lang="de">
<head>
<meta charset="utf-8">
<title>TIVARELCAP Zahnarztpraxis</title>
<link href="https://fonts.googleapis.com/css2?family=Open+Sans:wght@400;600&display=swap" rel="stylesheet">
<style>
:root{
  --navy:#07076a;
  --navy-dark:#030344;
  --top-grey:#cbcbcb;
  --page:#f2f2f2;
  --text:#444;
  --footer:#1c1c1c;
  --footer-text:#bdbdbd;
  --news-bg:#ebe8eb;
  --social:#5c5c66;
}
*{margin:0;padding:0;box-sizing:border-box}
html,body{width:972px;height:1200px;overflow:hidden}
body{font-family:"Open Sans",sans-serif;color:var(--text);background:var(--page);position:relative}
.abs{position:absolute}
.top-band{left:0;top:0;width:972px;height:186px;background:var(--top-grey)}
.logo{left:152px;top:42px;display:flex;align-items:center;gap:10px}
.logo-mark{width:44px;height:44px;background:#c99a3a;border-radius:50%}
.logo-name{font-size:24px;letter-spacing:1px;color:#555;line-height:1}
.logo-sub{left:232px;top:76px;font-size:19px;color:#555}
.lang{left:685px;top:71px;font-size:11px;color:#333;display:flex;align-items:center;gap:6px}
.flag{width:16px;height:10px;display:inline-block}
.flag-de{background:linear-gradient(#111 0 33%,#d00 33% 66%,#fc0 66%)}
.flag-en{background:#1a2d7a;position:relative}
.flag-en::before{content:"";position:absolute;left:6px;top:0;width:4px;height:10px;background:#d00;box-shadow:0 0 0 1px #fff}
.flag-en::after{content:"";position:absolute;left:0;top:3px;width:16px;height:4px;background:#d00;box-shadow:0 0 0 1px #fff}
.container{left:139px;top:134px;width:696px;height:963px;background:#fff;border-left:1px solid #ccc;border-right:1px solid #ccc}
.nav{left:139px;top:134px;width:696px;height:52px;background:var(--navy);display:flex;align-items:center}
.nav a{color:#fff;text-decoration:none;font-size:12px;height:52px;line-height:52px;padding:0 16px}
.nav a.active{background:var(--navy-dark);padding:0 24px}
.search{left:801px;top:154px}
.hero{left:139px;top:186px;width:696px;height:313px;background:linear-gradient(100deg,#c7b9a9 0%,#e8e3dc 35%,#9cc5cc 60%,#d9e7ee 100%)}
.caption{left:165px;top:419px;width:309px;height:63px;background:rgba(70,70,70,.82);color:#fff;padding:8px 6px}
.caption h3{font-size:10px;font-weight:400;margin-bottom:6px}
.caption p{font-size:7.5px;line-height:12px;color:#ddd}
.cap-ctrl{left:479px;top:465px;width:31px;height:16px;background:#555;color:#fff;font-size:7px;text-align:center;line-height:16px;letter-spacing:4px}
.dot{width:8px;height:8px;background:#999;top:474px}
.dot.on{background:var(--navy-dark)}
h2.sec{font-size:17px;font-weight:400;color:var(--navy)}
.svc-intro{left:156px;top:549px;width:180px;font-size:9.8px;line-height:21px}
.svc{top:534px;width:144px}
.svc .ph{height:77px;background:linear-gradient(120deg,#6fa6cc,#e3eef5)}
.svc h4{font-size:10.5px;font-weight:600;color:#333;margin:10px 0 6px -4px}
.svc p{font-size:10px;line-height:17px;margin-left:-4px}
.hr{left:161px;width:644px;height:1px;background:#ddd}
.welcome-photo{left:171px;top:763px;width:108px;height:88px;background:linear-gradient(135deg,#caa36a,#f0dcc4);border:2px solid #ddd;border-radius:2px}
.welcome-text{left:293px;top:763px;width:530px;font-size:9.8px;line-height:16.5px}
.welcome-text .sig{color:var(--navy);margin-top:5px}
h3.small{font-size:12px;font-weight:600;color:var(--navy)}
.avatar{left:164px;top:940px;width:87px;height:87px;border-radius:50%;background:linear-gradient(135deg,#8fb9d9,#e6eff5);border:2px solid #ccc}
.quote{left:264px;top:943px;width:340px;font-size:8.2px;line-height:15.5px;color:#222}
.quote .author{color:var(--navy);margin-top:18px}
.tdot{top:1051px;width:6px;height:6px;border-radius:50%;background:#bbb}
.news{left:615px;top:933px;width:198px;height:135px;background:var(--news-bg)}
.news .ph{position:absolute;left:8px;top:13px;width:59px;height:39px;background:linear-gradient(135deg,#6f9ec4,#e4eef6)}
.news h5{position:absolute;left:76px;top:13px;width:115px;font-size:9px;font-weight:400;line-height:16px;color:#222}
.news .date{position:absolute;left:77px;top:46px;font-size:6px;color:#999}
.news p{position:absolute;left:11px;top:67px;width:180px;font-size:7.5px;line-height:16.5px;color:#444}
.news .more{position:absolute;right:9px;top:113px;font-size:7.5px;color:var(--navy)}
.footer{left:0;top:1097px;width:972px;height:103px;background:var(--footer);color:var(--footer-text)}
.f-item{font-size:8.5px;line-height:17px;color:var(--footer-text)}
.social{top:1113px;width:20px;height:20px;border-radius:50%;background:var(--social)}
.social-label{top:1136px;font-size:5px;color:#aaa;width:30px;text-align:center}
.f-line{left:155px;top:1165px;width:660px;height:1px;background:#333}
.copy{top:1178px;font-size:8.5px;color:var(--footer-text)}
</style>
</head>
<body>
<div class="abs top-band"></div>
<div class="abs logo"><span class="logo-mark"></span><span class="logo-name">TIVARELCAP</span></div>
<div class="abs logo-sub">Zahnarztpraxis</div>
<div class="abs lang">Choose Language : <span class="flag flag-de"></span><span class="flag flag-en"></span></div>

<div class="abs container"></div>
<nav class="abs nav">
  <a class="active">Home</a><a>About Us</a><a>Services</a><a>News &amp; Events</a><a>Blog</a><a>Contact</a>
</nav>
<svg class="abs search" width="16" height="16" viewBox="0 0 16 16"><circle cx="6" cy="6" r="4.5" fill="none" stroke="#fff" stroke-width="2"/><line x1="9.5" y1="9.5" x2="15" y2="15" stroke="#fff" stroke-width="2.5"/></svg>

<div class="abs hero" role="img" aria-label="Smiling dental assistant in front, dentist treating a patient behind"></div>
<div class="abs caption"><h3>Lorem ipsum dolor sit amet, consectetuer adipiscing elit,</h3><p>Lorem ipsum dolor sit amet, consectetuer adipiscing elit, sed diam nonummy nibh euismod tincidunt ut laoreet dolore magna aliquam erat volutpat.</p></div>
<div class="abs cap-ctrl">‹›</div>
<div class="abs dot" style="left:754px"></div>
<div class="abs dot" style="left:775px"></div>
<div class="abs dot on" style="left:795px"></div>

<h2 class="abs sec" style="left:147px;top:516px">Our Services</h2>
<p class="abs svc-intro">Mauris at justo eu lectus auctor porta vel ut libero. Suspendisse mattis tellus vel augue mollis ultrices. Suspendisse potenti. Nunc erat enim, vestibulum.</p>
<div class="abs svc" style="left:358px"><div class="ph" role="img" aria-label="Dentist giving thumbs up in treatment room"></div><h4>Lorem ipsum dolor ipsukm</h4><p>Porta vel ut libero. Suspendisse mattis tellus vel augue mollis</p></div>
<div class="abs svc" style="left:518px"><div class="ph" role="img" aria-label="Dentist with smiling patient"></div><h4>Lorem ipsum dolor ipsukm</h4><p>Porta vel ut libero. Suspendisse mattis tellus vel augue mollis</p></div>
<div class="abs svc" style="left:677px"><div class="ph" role="img" aria-label="Dentist examining a child"></div><h4>Lorem ipsum dolor ipsukm</h4><p>Porta vel ut libero. Suspendisse mattis tellus vel augue mollis</p></div>

<div class="abs hr" style="top:704px"></div>
<h2 class="abs" style="left:147px;top:727px;font-size:17px;font-weight:400;color:#222">Herzlich willkommen in unserer neuen Praxis.</h2>
<div class="abs welcome-photo" role="img" aria-label="Portrait of the dentist"></div>
<div class="abs welcome-text">
  <p>Es ist unser Ziel, Ihr Wohlbefinden zu steigern. Sie sollen die Schönheit des Alltags mit gesunden Zähnen geniessen und in jeder Situation herzhaft lachen können.Es ist unser Ziel, Ihr Wohlbefinden zu steigern. Sie sollen die Schönheit des Alltags mit gesunden Zähnen geniessen und in jeder Situation herzhaft lachen können.</p>
  <p style="margin-top:5px">Ihre Zahnärztin</p>
  <p class="sig">Dr. med. dent. Lena Marti-Hofer</p>
</div>

<div class="abs hr" style="top:882px"></div>
<h3 class="abs small" style="left:160px;top:903px">Testmonials</h3>
<h3 class="abs small" style="left:606px;top:903px">Latest News</h3>
<svg class="abs" style="left:782px;top:904px" width="30" height="14" viewBox="0 0 30 14"><polyline points="7,1 2,7 7,13" fill="none" stroke="#222" stroke-width="1.3"/><polyline points="23,1 28,7 23,13" fill="none" stroke="#222" stroke-width="1.3"/></svg>
<div class="abs avatar" role="img" aria-label="Portrait of a patient giving a testimonial"></div>
<div class="abs quote"><p>Etiam iaculis imperdiets nibh, ac viverra telluset. Euismod aliquam. Pellentesque nisi tortor, elementum. Vitae posuere eget, ornare quis purustin lost rhoncus sagittis mattis. Vestibulum los egest tincidunt eget molestie quam,</p><p class="author">-Mara Keller, Example AG</p></div>
<div class="abs tdot" style="left:363px"></div>
<div class="abs tdot" style="left:371px;background:var(--navy)"></div>
<div class="abs tdot" style="left:379px"></div>
<div class="abs news">
  <div class="ph" role="img" aria-label="Dental instrument close-up"></div>
  <h5>Etiam iaculis imperdiets nibh, ac viverra telluset.</h5>
  <span class="date">Posted On : 15.2.2014</span>
  <p>Etiam iaculis imperdiets nibh ac viverra telluset tismod est aliquam. Pellentesque nisi tortor, elementum vivamus.</p>
  <span class="more">Read More..</span>
</div>

<footer class="abs footer"></footer>
<svg class="abs" style="left:157px;top:1126px" width="7" height="7" viewBox="0 0 8 8"><path d="M4 0 0 4h1v4h2V5h2v3h2V4h1z" fill="#bbb"/></svg>
<div class="abs f-item" style="left:167px;top:1121px">Lindenweg 12<br>CH-8600 Musterdorf</div>
<svg class="abs" style="left:271px;top:1123px" width="10" height="10" viewBox="0 0 10 10"><path d="M2 0 4 2 3 4Q4 6 6 7L8 6 10 8 8 10Q3 9 0 2Z" fill="#bbb"/></svg>
<svg class="abs" style="left:271px;top:1141px" width="11" height="9" viewBox="0 0 11 9"><rect x=".5" y=".5" width="10" height="8" fill="none" stroke="#bbb"/><polyline points=".5,.5 5.5,5 10.5,.5" fill="none" stroke="#bbb"/></svg>
<div class="abs f-item" style="left:286px;top:1121px">+41 (0)44 555 01 23<br>info@tivarel.ch</div>
<div class="abs social" style="left:667px"></div>
<div class="abs social" style="left:693px"></div>
<div class="abs social" style="left:721px"></div>
<div class="abs social" style="left:748px"></div>
<div class="abs social" style="left:775px"></div>
<div class="abs social" style="left:803px"></div>
<div class="abs social-label" style="left:662px">Follow</div>
<div class="abs social-label" style="left:688px">News</div>
<div class="abs social-label" style="left:716px">Video</div>
<div class="abs social-label" style="left:743px">Share</div>
<div class="abs social-label" style="left:770px">Network</div>
<div class="abs social-label" style="left:798px">Feed</div>
<div class="abs f-line"></div>
<div class="abs copy" style="left:147px">Copyright 2014 © TIVARELCAP | Dr. med. dent. L. Marti-Hofer. All rights reserved.</div>
<div class="abs copy" style="left:710px">Disclaimer | Privacy | Sitemap</div>
</body>
</html>
```